Need a tea box packaging design

* Organic Herbal tea
* Imported from india to france for european community
* our main rivals are " DORVE" tea and " BREN" tea.
* the product will be sold online and shops.
* 15 variety of teas will be imported.
* The details in the attached file.
The Packaging contents:
Main page :
Brand Name : SELVO ( logo attached)
Name of the product: KORINE THE VERT ( which means Korine green tea)
Type of the product : Infusion
No of tea bags : 20
Weight of each bag : 1,5 gm
Total weight : 30 gm
Organic label name : Europe ( organic logo attached)
vegan label : vegan ( vegan label attached)
The other side contents will be given later.
A model that i have designed with another designer is attached. It is nice. But i am expecting more than that. ( attached)
Some designs that i like are attached here.
As mentionned earlier there will 15 variety of teas, so the design should easily modifiable by just changing colours.
Project Deadline Extended Reason: I think the deadline is very short due to the weekend. So, I feel it is better to extend the deadline by 5 days. Added Saturday, January 21, 2017
Target Market(s)
Europe. Mainly france.
Industry/Entity Type
Community
Requirements
Must have
- * Design should be modern and colourfull.
- * I like pattern works, Vectorials
- * Yoga silouhaites in the design is appreciable.
- * The design should express wellness, joy and love
Nice to have
- "Dorve" tea in my inspirational design.
- * The ingredients can be showed in vectorial designs in the back ground.
- * The end user must see the box while taking the tea and appreciate
- * The end user must search and find some hidden things.
- * The box must be communicative.
- * Trendy frames.
Should not have
- No need to have tea cups

```html
<!DOCTYPE html>
<html lang="en">
<head>
<meta charset="utf-8">
<title>SELVO – Korine The Vert Infusion</title>
<link rel="stylesheet" href="https://fonts.googleapis.com/css2?family=Yanone+Kaffeesatz:wght@700&family=Exo+2:wght@400;500&display=swap">
<style>
  :root{
    --page:#e6e5e1;
    --label-dark:#1d2116;
    --label-light:#9dbb4d;
    --label-rim:#a6c85a;
    --band:#4f6b1c;
    --ink:#15180f;
    --white:#ffffff;
    --number:#e6ec7a;
    --lime:#c9df2a;
    --lime-deep:#aac21c;
    --orange:#ec6f1f;
    --orange-deep:#d3561a;
  }
  *{box-sizing:border-box;margin:0;padding:0}
  html,body{width:1146px;height:1200px;overflow:hidden}
  body{background:var(--page);font-family:"Exo 2",sans-serif;position:relative}

  .box-front{position:absolute;top:190px;width:500px;height:820px}
  .box-front--lime{left:48px;--panel:var(--lime);--panel-deep:var(--lime-deep)}
  .box-front--orange{left:598px;--panel:var(--orange);--panel-deep:var(--orange-deep)}

  .box-front__pattern{position:absolute;inset:0;
    background:radial-gradient(circle at 30% 25%,var(--panel) 0%,var(--panel-deep) 100%)}
  .box-front__frame{position:absolute;inset:12px;border:1.5px solid rgba(0,0,0,.25)}

  .label{position:absolute;left:55px;top:30px;width:390px;height:760px}
  .label__shape{position:absolute;inset:0}

  .brand{position:absolute;top:70px;left:0;right:0;display:flex;justify-content:center;align-items:center;gap:14px}
  .brand__name{font-family:"Exo 2",sans-serif;font-weight:500;font-size:66px;letter-spacing:4px;color:var(--white);line-height:1}
  .brand__dot{width:22px;height:22px;border-radius:50%;background:var(--label-light)}

  .product{position:absolute;top:268px;left:0;right:0;text-align:center;
    font-family:"Yanone Kaffeesatz",sans-serif;font-weight:700;color:var(--ink);line-height:.95}
  .product__line1{font-size:88px;display:flex;justify-content:center;align-items:center;gap:12px}
  .product__stars{font-size:20px;letter-spacing:3px}
  .product__line2{font-size:96px}

  .type-band{position:absolute;top:486px;left:22px;right:22px;height:46px;background:var(--band);
    display:flex;align-items:center;justify-content:center;
    font-family:"Exo 2",sans-serif;font-size:34px;font-weight:400;color:var(--white);letter-spacing:1px}

  .contents{position:absolute;top:600px;left:48px;right:30px;display:flex;align-items:flex-start;gap:44px;color:var(--white)}
  .contents__count{text-align:center;line-height:1}
  .contents__number{display:block;font-size:40px;color:var(--number)}
  .contents__unit{display:block;font-size:13px;margin-top:4px}
  .contents__weights{font-size:18px;line-height:1.5;padding-top:4px}

  .badges{position:absolute;top:686px;left:0;right:0;display:flex;justify-content:center;gap:30px}
  .badge{width:66px;height:66px;border-radius:50%}
  .badge--vegan{border:2px solid var(--label-light)}
  .badge--organic{background:var(--label-light)}
</style>
</head>
<body>

<article class="box-front box-front--lime">
  <div class="box-front__pattern" role="img" aria-label="Lime mandala pattern with yoga pose silhouettes"></div>
  <div class="box-front__frame"></div>
  <div class="label">
    <svg class="label__shape" viewBox="0 0 390 760" width="390" height="760">
      <path d="M40 6 H350 L384 54 V668 L296 754 H94 L6 668 V54 Z" fill="var(--label-dark)" stroke="var(--label-rim)" stroke-width="8"/>
      <rect x="22" y="238" width="346" height="330" fill="var(--label-light)"/>
      <line x1="22" y1="230" x2="368" y2="230" stroke="var(--label-rim)" stroke-width="3"/>
      <line x1="22" y1="576" x2="368" y2="576" stroke="var(--label-rim)" stroke-width="3"/>
    </svg>
    <div class="brand"><span class="brand__name">SELVO</span><span class="brand__dot"></span></div>
    <h1 class="product">
      <span class="product__line1"><span class="product__stars">•••</span>Korine<span class="product__stars">•••</span></span>
      <span class="product__line2">The Vert</span>
    </h1>
    <div class="type-band">INFUSION</div>
    <div class="contents">
      <div class="contents__count"><span class="contents__number">20</span><span class="contents__unit">Tea Bags</span></div>
      <div class="contents__weights">Each bag : 1.5 gm<br>Total weight : 30 gm</div>
    </div>
    <div class="badges">
      <span class="badge badge--vegan" role="img" aria-label="Vegan label"></span>
      <span class="badge badge--organic" role="img" aria-label="European organic label"></span>
    </div>
  </div>
</article>

<article class="box-front box-front--orange">
  <div class="box-front__pattern" role="img" aria-label="Orange mandala pattern with yoga pose silhouettes"></div>
  <div class="box-front__frame"></div>
  <div class="label">
    <svg class="label__shape" viewBox="0 0 390 760" width="390" height="760">
      <path d="M40 6 H350 L384 54 V668 L296 754 H94 L6 668 V54 Z" fill="var(--label-dark)" stroke="var(--label-rim)" stroke-width="8"/>
      <rect x="22" y="238" width="346" height="330" fill="var(--label-light)"/>
      <line x1="22" y1="230" x2="368" y2="230" stroke="var(--label-rim)" stroke-width="3"/>
      <line x1="22" y1="576" x2="368" y2="576" stroke="var(--label-rim)" stroke-width="3"/>
    </svg>
    <div class="brand"><span class="brand__name">SELVO</span><span class="brand__dot"></span></div>
    <h2 class="product">
      <span class="product__line1"><span class="product__stars">•••</span>Korine<span class="product__stars">•••</span></span>
      <span class="product__line2">The Vert</span>
    </h2>
    <div class="type-band">INFUSION</div>
    <div class="contents">
      <div class="contents__count"><span class="contents__number">20</span><span class="contents__unit">Tea Bags</span></div>
      <div class="contents__weights">Each bag : 1.5 gm<br>Total weight : 30 gm</div>
    </div>
    <div class="badges">
      <span class="badge badge--vegan" role="img" aria-label="Vegan label"></span>
      <span class="badge badge--organic" role="img" aria-label="European organic label"></span>
    </div>
  </div>
</article>

</body>
</html>
```